Business Cards Needed For Veterinary Business

Looking for a business card design for a veterinary blood bank. We would like it to be clean and professional on appearance but still warm and inviting. We would like to utilize our logo and similar coloring. We will use our phone number, email, website, employee name, employee title.

We do not want a bunch of animated animal photos but do not need the style to be as clinical as a laboratory or human medical procedure office.

We are looking for some creative ideas to choose from so that we can generate a standout professional business card for our management team to utilize.

Target Market(s)

professionals

Industry/Entity Type

veterinary

Contact Information for Business Card

employee name, employee title, phone number, website URL, email

Font styles to use
Sans Serif

Colors
0054AA
0677BA
7BADD7
CADEEF
E8F1F8
EB3D1F
EC4F4E
F09395
F8D3D4
FCEDEE

Requirements
Nice to have
• creative design
Should not have
• animated photos

```html
<!DOCTYPE html>
<html lang="en">
<head>
<meta charset="utf-8">
<title>Harbor Vale Animal Blood Bank – Business Card</title>
<link href="https://fonts.googleapis.com/css2?family=Montserrat:wght@500;700;800&family=Lato:wght@400;700&display=swap" rel="stylesheet">
<style>
  :root {
    --brand-blue: #0f4f9a;
    --brand-red: #e8202a;
    --ink-grey: #5a5a5a;
    --rule-grey: #e3e6ea;
    --card-white: #ffffff;
    --backdrop: #2b2d31;
  }
  * { box-sizing: border-box; margin: 0; padding: 0; }
  html, body { width: 1200px; height: 952px; overflow: hidden; }
  body {
    background: var(--backdrop);
    font-family: "Lato", sans-serif;
    position: relative;
  }
  .card {
    position: absolute;
    width: 540px;
    height: 309px;
    top: 322px;
    overflow: hidden;
    box-shadow: 0 14px 30px rgba(0,0,0,0.45);
  }
  /* Front */
  .card-front { left: 40px; background: var(--card-white); }
  .edge-bar-left {
    position: absolute; left: 0; top: 46px;
    width: 9px; height: 140px; background: var(--brand-blue);
  }
  .edge-bar-right {
    position: absolute; right: 0; bottom: 0;
    width: 18px; height: 108px; background: var(--brand-blue);
  }
  .brand-lockup {
    position: absolute; left: 38px; top: 78px;
    width: 190px;
    display: flex; align-items: center; gap: 9px;
  }
  .brand-dot {
    flex: none; width: 22px; height: 22px; border-radius: 50%;
    background: var(--brand-red);
  }
  .brand-name {
    font-family: "Montserrat", sans-serif; font-weight: 700;
    font-size: 15px; line-height: 1.2; color: var(--brand-blue);
    text-transform: uppercase; letter-spacing: 0.02em;
  }
  .divider {
    position: absolute; left: 245px; top: 62px;
    width: 1px; height: 140px; background: var(--rule-grey);
  }
  .contact-block { position: absolute; left: 268px; top: 74px; }
  .person-name {
    font-family: "Montserrat", sans-serif; font-weight: 500;
    font-size: 17px; color: var(--brand-red); letter-spacing: 0.02em;
  }
  .person-name strong { font-weight: 800; }
  .person-title { font-size: 13px; color: var(--ink-grey); margin-top: 3px; }
  .contact-list { list-style: none; margin-top: 14px; }
  .contact-list li {
    display: flex; align-items: center; gap: 8px;
    font-size: 12px; color: var(--ink-grey); margin-bottom: 6px;
  }
  .contact-list svg { width: 11px; height: 11px; fill: var(--brand-blue); flex: none; }
  .address {
    position: absolute; left: 38px; bottom: 34px;
    font-size: 11.5px; color: var(--ink-grey);
  }
  /* Back */
  .card-back {
    left: 620px; background: var(--brand-blue);
    display: flex; align-items: center; justify-content: center; gap: 14px;
  }
  .card-back .brand-dot { width: 40px; height: 40px; }
  .card-back .brand-name {
    color: var(--card-white); font-size: 24px; line-height: 1.15; width: 250px;
  }
</style>
</head>
<body>
  <section class="card card-front" aria-label="Business card front">
    <div class="edge-bar-left"></div>
    <div class="edge-bar-right"></div>
    <div class="brand-lockup">
      <span class="brand-dot"></span>
      <span class="brand-name">Harbor Vale Animal Blood Bank</span>
    </div>
    <div class="divider"></div>
    <div class="contact-block">
      <p class="person-name">DANIEL R. <strong>WHITFORD</strong></p>
      <p class="person-title">Managing Director</p>
      <ul class="contact-list">
        <li><svg viewBox="0 0 24 24"><path d="M6.6 10.8a15.1 15.1 0 0 0 6.6 6.6l2.2-2.2a1 1 0 0 1 1-.25 11.4 11.4 0 0 0 3.6.57 1 1 0 0 1 1 1V20a1 1 0 0 1-1 1A17 17 0 0 1 3 4a1 1 0 0 1 1-1h3.5a1 1 0 0 1 1 1c0 1.25.2 2.45.57 3.6a1 1 0 0 1-.25 1z"/></svg>+00 987 654 32</li>
        <li><svg viewBox="0 0 24 24"><path d="M2 5h20v14H2z M2 5l10 8 10-8" /></svg>hello@harborvaleabb.org</li>
        <li><svg viewBox="0 0 24 24"><circle cx="12" cy="12" r="10"/></svg>www.harborvaleabb.org</li>
      </ul>
    </div>
    <p class="address">1275 Lakeside Avenue Portland, OR 97205</p>
  </section>

  <section class="card card-back" aria-label="Business card back">
    <span class="brand-dot"></span>
    <span class="brand-name">Harbor Vale Animal Blood Bank</span>
  </section>
</body>
</html>
```